Luxury Ayurvedic Hair Oil logo and package design

We need a logo and package design for our Ayurvedic and natural hair growth oil. Our company, Velmora, is the premier luxury Ayurvedic beauty brand, bringing ancient East-Indian natural and botanic health and beauty products to the US market. Our first major product - Velmora Hair Growth Oil - is a coconut oil based product that was developed by tribes in the Southern State of Kerala that includes ancient herbs like Gooseberry, Indigo, Indian Aloe, Balloon Vine and Brahmi.

The design should be catered to the high-end luxury market (minimal design, minimal text, fonts that invoke a sense of luxury). The primary colors should be deep blue for the packaging and gold for the characters (it's in the name - Velmora). We are looking to sell our products in Brenvale and Tolland Pryce and require packaging that is in line with products sold at these high-end retailers.

The final logo design and packaging should communicate luxury and the ancient wisdom of far-eastern traditions.

Target Market(s)

Velmora's main target is women who value fashionable/quality skincare, beauty, and fragrance products and are open to a medium to high price range. These women love uniqueness in brand and products that cannot be found elsewhere. They are looking for the next new "it" item that will take their haircare and beauty regiment to the next level.

Industry/Entity Type

Hair And Beauty

Font styles to use
Serif

Colors
2f73b3
ffc214

Requirements
Must have
• Must use deep blue (royal blue) background and gold text (to align with brand name). Must use luxurious fonts
Nice to have
• Flowers or other natural symbols, pictures that blend well with the product theme

```html
<!DOCTYPE html>
<html lang="en">
<head>
<meta charset="utf-8">
<title>Velmora Ayurvedic Natural Hair Growth Oil – Label</title>
<link rel="stylesheet" href="https://fonts.googleapis.com/css2?family=Italiana&family=Montserrat:wght@400&display=swap">
<style>
  :root {
    --page: #ffffff;
    --navy: #07065a;
    --gold: #cdb07a;
    --gold-soft: #d7c9a6;
    --gold-glow: rgba(205, 176, 122, 0.18);
    --gold-fade: rgba(205, 176, 122, 0);
  }
  * { margin: 0; padding: 0; box-sizing: border-box; }
  html, body {
    width: 1200px;
    height: 1200px;
    overflow: hidden;
    background: var(--page);
  }
  .canvas {
    position: relative;
    width: 1200px;
    height: 1200px;
  }
  .label {
    position: absolute;
    left: 382px;
    top: 60px;
    width: 436px;
    height: 1080px;
    background: var(--navy);
    color: var(--gold);
    text-align: center;
    overflow: hidden;
  }
  .brand-name {
    position: absolute;
    top: 158px;
    left: 0;
    right: 0;
    font-family: "Italiana", serif;
    font-weight: 400;
    font-size: 50px;
    line-height: 1;
  }
  .range-title {
    position: absolute;
    top: 342px;
    left: 0;
    right: 0;
    font-family: "Italiana", serif;
    font-weight: 400;
    font-size: 35px;
    line-height: 1;
    letter-spacing: 0.5px;
  }
  .product-name {
    position: absolute;
    top: 488px;
    left: 0;
    right: 0;
    font-family: "Italiana", serif;
    font-size: 30px;
    line-height: 38px;
  }
  .ingredients {
    position: absolute;
    top: 616px;
    left: 0;
    right: 0;
    list-style: none;
    font-family: "Montserrat", sans-serif;
    font-size: 14px;
    line-height: 18.5px;
    color: var(--gold-soft);
  }
  .botanical-art {
    position: absolute;
    left: 60px;
    top: 770px;
    width: 330px;
    height: 310px;
    background: radial-gradient(ellipse closest-side at 50% 55%, var(--gold-glow), var(--gold-fade) 100%);
  }
</style>
</head>
<body>
  <main class="canvas">
    <section class="label">
      <h1 class="brand-name">Velmora</h1>
      <h2 class="range-title">AYURVEDIC</h2>
      <p class="product-name">NATURAL HAIR<br>GROWTH OIL</p>
      <ul class="ingredients">
        <li>COCONUT OIL</li>
        <li>GOOSEBERRY</li>
        <li>INDIGO</li>
        <li>INDIAN ALOE</li>
        <li>BALLOON VINE</li>
        <li>BRAHMI</li>
      </ul>
      <div class="botanical-art" role="img" aria-label="Gold line illustration of leafy branches and a small flowering sprig"></div>
    </section>
  </main>
</body>
</html>
```